New business card/stationary for a consulting company

I am looking for a clean and very professional looking business card for my consulting company as well as corresponding stationary. I am uploading our logo. I like simple and powerful for the feel. No graphics but I am open on everything else. Below is my contact information but would like the final to be in a version I can add my employees information into and print. Thank you.

Daniel Whitcombe
dan@fernlowadvisory.com
2837 North 9th Avenue, Summit Floor, Oak Brook, Illinois 60483
www.fernlowadvisory.com

Industry/Entity Type

Consulting

Contact Information for Business Card

Daniel Whitcombe
dan@fernlowadvisory.com
www.fernlowadvisory.com

Font styles to use
Serif
Sans Serif

Requirements
Must have
• Our logo and the business card details.
Nice to have
• our website www.fernlowadvisory.com

```html
<!DOCTYPE html>
<html lang="en">
<head>
<meta charset="utf-8">
<title>Fernlow Advisory – Business Card</title>
<link rel="stylesheet" href="https://fonts.googleapis.com/css2?family=Questrial&family=Lato:wght@400;700&display=swap">
<style>
  :root {
    --navy: #221f5f;
    --white: #ffffff;
    --paper: #f1f0f5;
    --backdrop: #e7e4de;
    --ink-light: #f4f4fa;
  }
  * { box-sizing: border-box; margin: 0; padding: 0; }
  html, body { width: 900px; height: 1200px; overflow: hidden; }
  body { background: var(--backdrop); position: relative; font-family: "Questrial", sans-serif; }

  .card { position: absolute; border-radius: 18px; overflow: hidden; }

  /* Front */
  .card-front { left: 82px; top: 133px; width: 733px; height: 430px; background: var(--white); }
  .card-front .pattern-area { position: absolute; inset: 0; background: var(--paper); }
  .card-front .brand-mark {
    position: absolute; left: 344px; top: 284px; width: 46px; height: 46px;
    background: var(--navy);
  }
  .card-front .brand-mark { left: 344px; top: 160px; }
  .card-front .brand-name {
    position: absolute; left: 0; right: 0; top: 240px; text-align: center;
    color: var(--navy); font-size: 38px; letter-spacing: 0.5px;
  }
  .card-front .web-band {
    position: absolute; left: 0; right: 0; top: 377px; height: 28px;
    background: var(--navy); color: var(--white);
    font-family: "Lato", sans-serif; font-weight: 700; font-size: 15px; letter-spacing: 1px;
    text-align: center; line-height: 28px;
  }

  /* Back */
  .card-back { left: 88px; top: 630px; width: 734px; height: 430px; background: var(--navy); color: var(--white); }
  .person-name { position: absolute; left: 43px; top: 52px; font-size: 21px; letter-spacing: 1.5px; }
  .person-title { position: absolute; left: 43px; top: 80px; font-size: 15px; letter-spacing: 1.2px; }
  .rule { position: absolute; top: 141px; height: 2px; background: var(--white); }
  .rule-left { left: 0; width: 457px; }
  .rule-right { left: 610px; width: 124px; }
  .back-mark { position: absolute; left: 566px; top: 120px; width: 36px; height: 36px; background: var(--white); }
  .back-name { position: absolute; right: 35px; top: 162px; font-size: 25px; letter-spacing: 0.6px; }

  .contact-list { position: absolute; left: 40px; top: 298px; list-style: none; font-family: "Lato", sans-serif; font-size: 18px; }
  .contact-list li { display: flex; align-items: center; height: 29px; }
  .contact-list svg { width: 20px; height: 20px; margin-right: 14px; fill: var(--white); }
  .address { position: absolute; right: 35px; top: 302px; text-align: right; font-family: "Lato", sans-serif; font-size: 18px; line-height: 26px; font-style: normal; }
</style>
</head>
<body>
  <section class="card card-front">
    <div class="pattern-area" role="img" aria-label="Faint repeated brand-name pattern background"></div>
    <div class="brand-mark"></div>
    <div class="brand-name">FERNLOW ADVISORY</div>
    <div class="web-band">WWW.FERNLOWADVISORY.COM</div>
  </section>

  <section class="card card-back">
    <div class="person-name">DANIEL WHITCOMBE</div>
    <div class="person-title">MANAGING DIRECTOR</div>
    <div class="rule rule-left"></div>
    <div class="back-mark"></div>
    <div class="rule rule-right"></div>
    <div class="back-name">FERNLOW ADVISORY</div>

    <ul class="contact-list">
      <li>
        <svg viewBox="0 0 20 20" aria-hidden="true"><path d="M3 7c0-2 3-3 7-3s7 1 7 3v1h-4V6.5H7V8H3z"/><path d="M5 9h10l2 6H3z"/></svg>
        7753-6620-4185
      </li>
      <li>
        <svg viewBox="0 0 20 20" aria-hidden="true"><path d="M2 5h16v10H2z M3.5 6.5v.3L10 11l6.5-4.2v-.3z M3.5 8.6v5h13v-5L10 12.8z" fill-rule="evenodd"/></svg>
        dan@fernlowadvisory.com
      </li>
      <li>
        <svg viewBox="0 0 20 20" aria-hidden="true"><circle cx="10" cy="10" r="8"/><path d="M6 6c2 1 2 3 4 3s1 3 3 3M12 4c0 2 2 2 3 3" stroke="#221f5f" stroke-width="1.6" fill="none"/></svg>
        www.fernlowadvisory.com
      </li>
    </ul>

    <address class="address">
      2837 North 9th Avenue<br>
      Summit Floor, Oak Brook<br>
      Illinois 60483
    </address>
  </section>
</body>
</html>
```